Modern business card design for professional copywriter

I'd like a business card design that I can use to have my cards printed out by plink.com as a squared corners business card (see artwork and design guidelines here: https://help.plink.com/hc/en-gb/sections/300481726-PLINK-Product-Templates)

The design should be clean and modern and reflect the colours, tone and branding on my website: https://noravestrel.com.au

Target Market(s)

Professionals, B2B small business owners

Industry/Entity Type

Business

Contact Information for Business Card

Nora Vestrel
m: 0427 593 864
e: nora@noravestrel.com.au
w: noravestrel.com.au

Font styles to use
Sans Serif

Requirements
Must have
• Tagline: "Smart copywriting for clever business people"
• Brand colours: fd8000, 009984, 666666 and black
Nice to have

```html
<!DOCTYPE html>
<html lang="en">
<head>
<meta charset="utf-8">
<title>Nora Vestrel – Business Card</title>
<link rel="stylesheet" href="https://fonts.googleapis.com/css2?family=Poppins:wght@400;500;600&display=swap">
<style>
  :root {
    --teal: #009984;
    --orange: #fd8000;
    --ink: #111111;
    --grey: #666666;
    --paper: #ffffff;
  }
  * { margin: 0; padding: 0; box-sizing: border-box; }
  html, body { width: 1200px; height: 804px; overflow: hidden; background: var(--paper); }
  .card {
    position: relative;
    width: 1200px;
    height: 804px;
    background: var(--paper);
    font-family: "Poppins", sans-serif;
    color: var(--ink);
  }
  .identity {
    position: absolute;
    right: 78px;
    top: 96px;
    text-align: right;
  }
  .identity__name {
    font-size: 50px;
    font-weight: 600;
    letter-spacing: 1px;
    line-height: 1.1;
    color: var(--teal);
  }
  .identity__role {
    font-size: 33px;
    font-weight: 400;
    line-height: 1.2;
    color: var(--ink);
  }
  .rule { position: absolute; right: 78px; height: 4px; }
  .rule--orange { top: 224px; width: 288px; background: var(--orange); }
  .rule--teal { top: 241px; width: 348px; background: var(--teal); }
  .side-bar { position: absolute; top: 290px; width: 8px; height: 240px; }
  .side-bar--left { left: 30px; background: var(--teal); }
  .side-bar--right { left: 1182px; background: var(--orange); }
  .brand {
    position: absolute;
    left: 112px;
    top: 372px;
    display: flex;
    flex-direction: column;
    gap: 10px;
  }
  .brand__lockup {
    display: flex;
    align-items: center;
    gap: 18px;
  }
  .brand__dot {
    width: 44px; height: 44px;
    border-radius: 50%;
    background: var(--orange);
  }
  .brand__name {
    font-size: 54px;
    font-weight: 500;
    color: var(--teal);
    line-height: 1;
  }
  .brand__tagline {
    font-size: 18px;
    font-weight: 400;
    line-height: 1.3;
    color: var(--grey);
    padding-left: 62px;
  }
  .contacts {
    position: absolute;
    right: 74px;
    top: 540px;
    list-style: none;
  }
  .contacts__item {
    display: flex;
    justify-content: flex-end;
    align-items: center;
    gap: 14px;
    height: 69px;
    font-size: 39px;
    font-weight: 400;
    color: var(--ink);
  }
  .contacts__icon { width: 44px; height: 44px; flex: none; }
</style>
</head>
<body>
  <main class="card">
    <header class="identity">
      <h1 class="identity__name">NORA VESTREL</h1>
      <p class="identity__role">Copywriter</p>
    </header>
    <div class="rule rule--orange"></div>
    <div class="rule rule--teal"></div>

    <div class="side-bar side-bar--left"></div>
    <div class="side-bar side-bar--right"></div>

    <div class="brand">
      <div class="brand__lockup">
        <span class="brand__dot"></span>
        <span class="brand__name">Nora Vestrel</span>
      </div>
      <p class="brand__tagline">Smart copywriting for clever business people</p>
    </div>

    <ul class="contacts">
      <li class="contacts__item">
        <span>0427 593 864</span>
        <svg class="contacts__icon" viewBox="0 0 44 44" aria-hidden="true">
          <rect x="12" y="3" width="20" height="38" rx="4" fill="none" stroke="var(--teal)" stroke-width="3"/>
          <line x1="19" y1="35" x2="25" y2="35" stroke="var(--teal)" stroke-width="3" stroke-linecap="round"/>
        </svg>
      </li>
      <li class="contacts__item">
        <span>nora@noravestrel.com.au</span>
        <svg class="contacts__icon" viewBox="0 0 44 44" aria-hidden="true">
          <rect x="2" y="9" width="40" height="27" fill="var(--orange)"/>
          <polyline points="2,10 22,25 42,10" fill="none" stroke="var(--paper)" stroke-width="2.5"/>
        </svg>
      </li>
      <li class="contacts__item">
        <span>noravestrel.com.au</span>
        <svg class="contacts__icon" viewBox="0 0 44 44" aria-hidden="true">
          <circle cx="22" cy="22" r="19" fill="var(--teal)"/>
          <g fill="none" stroke="var(--paper)" stroke-width="2">
            <ellipse cx="22" cy="22" rx="8" ry="19"/>
            <line x1="3" y1="22" x2="41" y2="22"/>
            <path d="M7 12 H37 M7 32 H37"/>
            <line x1="22" y1="3" x2="22" y2="41"/>
          </g>
        </svg>
      </li>
    </ul>
  </main>
</body>
</html>
```